For Lease sign for Property management company in Kansas City

We need someone to take our information and design a standard for lease sign that we can put in front of each of our buildings. I would love for it to do its job of letting people know there are units available but also be unique somehow. Also the aspect ratio of the design would ideally be 4 wide by 3 tall but we open to other ideas. It will be a larger yard sign.

Target Market(s)

Potential Tenants

Industry/Entity Type

Real Estate Development

Font styles to use
Sans Serif

Requirements
Must have
• Our logo, our website (www.quillstead-properties.com), our phone number (816) 555-2719.
Nice to have
• Some how say "For Lease"
Sign to be 4' wide by 3' tall
If there was a place to put the building name that would be cool but not ne
Should not have
• Nothing that I can think of

```html
<!DOCTYPE html>
<html lang="en">
<head>
<meta charset="utf-8">
<title>For Lease Yard Sign</title>
<link href="https://fonts.googleapis.com/css2?family=Montserrat:wght@400;600;700;800&family=Arimo:wght@700&display=swap" rel="stylesheet">
<style>
  :root {
    --board: #bababa;
    --brand-red: #be2430;
    --red-deep: #8f1a22;
    --gold: #f6b33a;
    --ink-grey: #555555;
    --panel-light: #f7f7f7;
    --panel-edge: #e6e6e6;
    --strip-dark: #3a3a3a;
    --white: #ffffff;
  }
  * { margin: 0; padding: 0; box-sizing: border-box; }
  html, body { width: 1200px; height: 944px; overflow: hidden; }
  body {
    background: var(--board);
    position: relative;
    font-family: "Montserrat", sans-serif;
  }
  .sign {
    position: absolute;
    left: 95px; top: 88px;
    width: 1010px; height: 753px;
    background: linear-gradient(90deg, var(--panel-edge), var(--panel-light) 50%, var(--panel-edge));
    box-shadow: 4px 6px 8px rgba(0,0,0,0.35);
    overflow: hidden;
  }
  .hero-photo {
    position: absolute;
    left: 0; top: 0;
    width: 1010px; height: 444px;
    background: linear-gradient(100deg, var(--red-deep) 0%, var(--brand-red) 35%, #a81e28 60%, var(--red-deep) 100%);
  }
  .headline-box {
    position: absolute;
    left: 113px; top: 105px;
    width: 780px; height: 141px;
    background: var(--white);
    display: flex; align-items: center; justify-content: center;
  }
  .headline {
    color: var(--brand-red);
    font-weight: 800;
    font-size: 114px;
    letter-spacing: -1px;
    line-height: 1;
    text-shadow: inset 0 0 0 #000;
    filter: drop-shadow(1px 2px 1px rgba(0,0,0,0.25));
  }
  .phone {
    position: absolute;
    left: 0; top: 270px;
    width: 1010px;
    text-align: center;
    color: var(--white);
    font-weight: 800;
    font-size: 64px;
    line-height: 1.2;
    text-shadow: 3px 4px 4px rgba(0,0,0,0.45);
  }
  .availability-tag {
    position: absolute;
    left: 606px; top: 409px;
    width: 291px; height: 37px;
    background: var(--gold);
    clip-path: polygon(12px 0, 100% 0, 100% 100%, 0 100%);
    display: flex; align-items: center; justify-content: center;
    padding-left: 24px;
    color: var(--white);
    font-family: "Arimo", sans-serif;
    font-weight: 700;
    font-size: 29px;
    text-shadow: 2px 2px 2px rgba(0,0,0,0.55);
  }
  .brand {
    position: absolute;
    left: 272px; top: 494px;
    display: flex; align-items: center; gap: 24px;
  }
  .brand-dot {
    width: 133px; height: 133px;
    border-radius: 50%;
    background: var(--gold);
    flex: none;
  }
  .brand-name {
    color: var(--brand-red);
    font-weight: 700;
    font-size: 46px;
    line-height: 1.05;
    letter-spacing: 1px;
  }
  .website {
    position: absolute;
    left: 251px; top: 662px;
    width: 506px; height: 40px;
    border: 1px solid #8a8a8a;
    display: flex; align-items: center; justify-content: center;
    color: var(--ink-grey);
    font-weight: 700;
    font-size: 27px;
    letter-spacing: 0.3px;
  }
  .base-strip {
    position: absolute;
    left: 0; bottom: 0;
    width: 1010px; height: 13px;
  }
  .caption {
    position: absolute;
    left: 0; top: 877px;
    width: 1200px;
    text-align: center;
    color: #5a5a5a;
    font-size: 14px;
    font-weight: 400;
  }
</style>
</head>
<body>
  <main class="sign">
    <div class="hero-photo" role="img" aria-label="Modern apartment buildings photograph tinted in brand red"></div>
    <div class="headline-box"><h1 class="headline">FOR LEASE</h1></div>
    <p class="phone">Call (816) 555-2719</p>
    <div class="availability-tag">Units Available</div>

    <div class="brand">
      <span class="brand-dot"></span>
      <p class="brand-name">QUILLSTEAD<br>PROPERTIES</p>
    </div>

    <p class="website">www.quillstead-properties.com</p>

    <svg class="base-strip" viewBox="0 0 1010 13" preserveAspectRatio="none" aria-hidden="true">
      <rect x="0" y="0" width="490" height="13" fill="#b0202b"/>
      <polygon points="490,13 502,0 512,0 500,13" fill="#ffffff"/>
      <rect x="512" y="0" width="498" height="13" fill="#3a3a3a" role="img" aria-label="Building photograph strip in grey"/>
      <polygon points="500,13 512,0 512,13" fill="#3a3a3a"/>
    </svg>
  </main>
  <p class="caption">Design Concept 1</p>
</body>
</html>
```